Motorcycle Shop Business Card

New business card for Motorcycle repair and customization shop.Business name: Copper Falcon Chris Morris443-865-5190, 7214 Quarry Lane Arbutus, MD 21227. www.dale@copperfalconcustoms.example. I uploaded some motorcycle images and logo and a couple of our calendar shoots. They do not have to be used on card just examples of some of our work and past graphic work.
We work on Vantor Brennick and Custom Built Motorcycles.

Looking for front and back design

Target Market(s)

Motorcycle owners

Industry/Entity Type

Motorcycle Part

```html
<!DOCTYPE html>
<html lang="en">
<head>
<meta charset="utf-8">
<title>Copper Falcon Customs – Business Card</title>
<link rel="stylesheet" href="https://fonts.googleapis.com/css2?family=Poppins:wght@400;700;800&display=swap">
<style>
  :root {
    --card-blue: #0040ff;
    --ink: #000000;
    --icon-grey: #9ea3aa;
    --divider: rgba(190, 195, 205, 0.75);
  }
  * { margin: 0; padding: 0; box-sizing: border-box; }
  html, body {
    width: 1200px;
    height: 720px;
    overflow: hidden;
    background: var(--card-blue);
  }
  .card {
    position: relative;
    width: 1200px;
    height: 720px;
    background: var(--card-blue);
    font-family: "Poppins", sans-serif;
    color: var(--ink);
  }
  .brand {
    position: absolute;
    left: 50px;
    top: 280px;
    width: 560px;
    text-align: center;
    font-weight: 700;
    line-height: 1.15;
    color: var(--ink);
  }
  .brand-name { display: block; font-size: 60px; letter-spacing: 1px; }
  .brand-tag { display: block; font-size: 60px; letter-spacing: 8px; }
  .divider {
    position: absolute;
    left: 626px;
    top: 172px;
    width: 3px;
    height: 378px;
    background: linear-gradient(to bottom, transparent, var(--divider) 12%, var(--divider) 88%, transparent);
  }
  .person-name {
    position: absolute;
    left: 652px;
    top: 206px;
    font-size: 64px;
    font-weight: 800;
    letter-spacing: 0.5px;
    line-height: 1;
    white-space: nowrap;
  }
  .contact-list {
    position: absolute;
    left: 652px;
    top: 298px;
    list-style: none;
  }
  .contact-item {
    display: flex;
    align-items: center;
    height: 46px;
    font-size: 25px;
    font-weight: 400;
    white-space: nowrap;
  }
  .contact-item .icon {
    width: 38px;
    height: 38px;
    margin-right: 23px;
    flex-shrink: 0;
  }
  .contact-item.address {
    align-items: flex-start;
    margin-top: 8px;
    height: auto;
  }
  .contact-item.address .text {
    font-size: 21px;
    line-height: 30px;
    text-transform: uppercase;
  }
  .icon path, .icon circle, .icon rect { fill: var(--icon-grey); }
</style>
</head>
<body>
<main class="card">
  <div class="brand">
    <span class="brand-name">COPPER FALCON</span>
    <span class="brand-tag">CUSTOMS</span>
  </div>

  <div class="divider"></div>

  <h1 class="person-name">DALE FENWICK</h1>

  <ul class="contact-list">
    <li class="contact-item phone">
      <svg class="icon" viewBox="0 0 38 38" aria-hidden="true">
        <path d="M4 13c0-5 7-8 15-8s15 3 15 8v3h-7v-3c-2-1-5-1.5-8-1.5s-6 .5-8 1.5v3H4z"/>
        <rect x="7" y="18" width="24" height="16" rx="3"/>
        <circle cx="19" cy="24" r="4" style="fill:var(--card-blue)"/>
      </svg>
      <span class="text">410-555-0137</span>
    </li>
    <li class="contact-item email">
      <svg class="icon" viewBox="0 0 38 38" aria-hidden="true">
        <rect x="3" y="8" width="32" height="22" rx="2"/>
        <path d="M4 9l15 12 15-12v3L19 24 4 12z" style="fill:var(--card-blue)"/>
      </svg>
      <span class="text">dale@copperfalconcustoms.example</span>
    </li>
    <li class="contact-item web">
      <svg class="icon" viewBox="0 0 38 38" aria-hidden="true">
        <circle cx="19" cy="19" r="16"/>
        <path d="M10 11c4 0 6 2 5 5s-4 3-3 7-3 4-4 2c-2-4-1-10 2-14zM22 8c5 1 9 5 9 10-3 0-5 2-5 5s-3 6-6 5c1-3 0-5-2-6s0-5 3-5 3-3 1-5z" style="fill:var(--card-blue)"/>
      </svg>
      <span class="text">www.copperfalconcustoms.example</span>
    </li>
    <li class="contact-item address">
      <svg class="icon" viewBox="0 0 38 38" aria-hidden="true">
        <path d="M19 2c-7 0-12 5-12 12 0 9 12 22 12 22s12-13 12-22c0-7-5-12-12-12z"/>
        <circle cx="19" cy="14" r="4.5" style="fill:var(--card-blue)"/>
      </svg>
      <span class="text">7214 Quarry Lane Larkmoor,<br>MD 21999.</span>
    </li>
  </ul>
</main>
</body>
</html>
```